Craft Beer Company

We need a web design for our Tampa based craft beer company that shows and tells what we are about and our products, up and coming beers, events and happenings. Must has a verify age by selecting yes or no to "are you 21 years or older.. have logos and product labels etc... currently have Pixaro.com a our website, thats under construction.
Target Market(s)
Craft Beer Enthusiasts , Craft Beer Community
Industry/Entity Type
Construction
Requirements
Must have
- The pages on the site should have, about us, events, our beer, store for e-commerce
being that we are set up with Pixaro.com I would like to contineu to use them, unless there is another option available. We have the domain there.

```html
<!DOCTYPE html>
<html lang="en">
<head>
<meta charset="utf-8">
<title>Harborline Brewing — Craft Beer Company</title>
<link rel="stylesheet" href="https://fonts.googleapis.com/css2?family=Open+Sans:wght@400;600;700&display=swap">
<style>
:root{
  --page:#f6f6f6;
  --card:#eeeeee;
  --ink:#2f2f2f;
  --muted:#666666;
  --green:#5f9e22;
  --green-btn:#3f8a17;
  --brown:#8a5a2c;
  --nav:#12241a;
  --footer:#1c1c1c;
  --white:#ffffff;
  --link:#3a5aa0;
  --accent-name:#b8862e;
}
*{box-sizing:border-box;margin:0;padding:0}
html,body{width:741px;height:1200px;overflow:hidden}
body{position:relative;background:var(--page);font-family:"Open Sans",Arial,sans-serif;color:var(--ink)}
.abs{position:absolute}
.topline{left:0;top:0;width:741px;height:2px;background:linear-gradient(90deg,#222 0 20%,var(--green) 20% 40%,#b08a5a 40% 60%,#333 60% 80%,var(--green) 80%)}
.search{left:80px;top:42px;width:88px;height:19px;background:#e4e4e4}
.search-btn{left:168px;top:42px;width:23px;height:19px;background:var(--green-btn)}
.brand-dot{left:358px;top:10px;width:24px;height:24px;border-radius:50%;background:var(--green)}
.brand{left:300px;top:38px;width:140px;text-align:center;font-size:15px;font-weight:700;color:var(--green);line-height:1.2}
.cart-icon{left:551px;top:42px}
.cart-title{left:583px;top:41px;font-size:9px;color:#555}
.cart-count{left:583px;top:56px;font-size:9px;color:var(--green)}
.nav{left:80px;top:106px;width:581px;height:37px;background:var(--nav)}
.nav a{position:absolute;top:15px;font-size:9px;color:#ddd;text-decoration:none;transform:translateX(-50%)}
.nav a.active{color:var(--green)}
.nav a.active::before{content:"";position:absolute;left:-4px;right:-4px;top:-10px;height:1px;background:var(--green)}
.hero{left:0;top:143px;width:741px;height:299px;background:linear-gradient(180deg,#3a3340 0%,#6a4f55 40%,#8a5e48 70%,#3a2e2a 100%)}
.hero-text{left:178px;top:154px;width:390px;text-align:center;font-size:9px;color:#ccc;line-height:15px}
.hero-arrow{top:142px;width:28px;height:26px;background:rgba(255,255,255,.25)}
.card{background:var(--card)}
.h3{font-size:16px;font-weight:400;color:var(--ink);text-align:center}
.h3 em{font-style:normal;color:var(--green)}
.small{font-size:8px;line-height:13px;color:var(--muted)}
.btn{font-size:8px;color:#e8e8e8;text-align:center;line-height:20px}
.btn.green{background:var(--green-btn)}
.btn.brown{background:var(--brown)}
.date{width:28px;height:25px;background:var(--brown);color:#eee;font-size:11px;font-weight:700;text-align:center;line-height:25px}
.avatar{width:28px;height:28px;border-radius:50%;background:#bdbdbd}
.feed-name{font-size:8px;color:var(--accent-name)}
.feed-text{font-size:7px;line-height:11px}
.feed-link{font-size:7px;color:var(--link);font-weight:600}
.prod-card{background:#f2f2f2;width:164px;height:228px}
.prod-img{height:128px;background:linear-gradient(160deg,#cfcac2,#8a6a48 55%,#bcb6ac)}
.prod-name{font-size:12px;text-align:center;color:var(--ink)}
.price{font-size:12px;color:var(--green);font-weight:600}
.footer{left:0;top:1150px;width:741px;height:50px;background:var(--footer)}
.copy{left:82px;top:1170px;font-size:7.5px;color:#999}
.social{top:1166px;width:19px;height:19px;border-radius:50%;background:#e5e5e5}
.backdrop{left:0;top:0;width:741px;height:1200px;background:rgba(0,0,0,.62)}
.modal{left:240px;top:213px;width:261px;height:145px;background:var(--white)}
.modal-bottle{left:16px;top:9px;width:40px;height:136px;background:linear-gradient(180deg,#4a2e1e 0%,#3a2214 40%,#d89a3a 60%,#2e1a10 100%);border-radius:12px 12px 3px 3px}
.modal-dot{left:140px;top:14px;width:24px;height:24px;border-radius:50%;background:var(--green)}
.modal-brand{left:112px;top:41px;width:80px;text-align:center;font-size:11px;font-weight:700;color:var(--green);line-height:1.2}
.modal-q{left:80px;top:79px;width:154px;text-align:center;font-size:12px;color:#222}
.radio{top:104px;font-size:9px;color:#333;display:flex;align-items:center;gap:8px}
.radio i{display:inline-block;width:8px;height:8px;border-radius:50%;border:1px solid #999;background:#fff;position:relative}
.radio i.on::after{content:"";position:absolute;left:1.5px;top:1.5px;width:3px;height:3px;border-radius:50%;background:#2d5fb0}
.close{left:236px;top:12px;width:17px;height:17px;border-radius:50%;background:#e6e6e6;font-size:9px;font-weight:700;text-align:center;line-height:17px;color:#222}
</style>
</head>
<body>
<div class="abs topline"></div>

<header>
  <div class="abs search"></div>
  <div class="abs search-btn"><svg width="23" height="19"><circle cx="11" cy="9" r="3" fill="none" stroke="#111" stroke-width="1.3"/><line x1="13" y1="11" x2="15" y2="13" stroke="#111" stroke-width="1.3"/></svg></div>
  <div class="abs brand-dot"></div>
  <div class="abs brand">Harborline<br>Brewing</div>
  <svg class="abs cart-icon" width="24" height="20"><path d="M1 2h4l3 11h12l2-8H7" fill="none" stroke="#333" stroke-width="2"/><circle cx="9" cy="17" r="2" fill="#333"/><circle cx="19" cy="17" r="2" fill="#333"/></svg>
  <div class="abs cart-title">My Shopping Cart</div>
  <div class="abs cart-count">(0) Item</div>
  <nav class="abs nav">
    <a class="active" style="left:102px">Home</a>
    <a style="left:173px">About</a>
    <a style="left:243px">Services</a>
    <a style="left:321px">Products</a>
    <a style="left:391px">News</a>
    <a style="left:468px">Contact Us</a>
  </nav>
</header>

<section class="abs hero" role="img" aria-label="Tampa city skyline at dusk">
  <div class="abs hero-arrow" style="left:0"></div>
  <div class="abs hero-arrow" style="left:713px"></div>
  <p class="abs hero-text">Harborline Brewing brings Tampa artisan craft beer to local taps and tables.</p>
</section>

<section>
  <div class="abs card" style="left:80px;top:472px;width:186px;height:152px"></div>
  <svg class="abs" style="left:154px;top:487px" width="38" height="38"><circle cx="19" cy="19" r="18" fill="none" stroke="var(--green)" stroke-width="1.5"/><rect x="16" y="16" width="6" height="12" rx="1.5" fill="var(--green)"/><rect x="17.5" y="11" width="3" height="6" fill="var(--green)"/></svg>
  <h3 class="abs h3" style="left:80px;top:533px;width:186px">Upcoming <em>Beers</em></h3>
  <p class="abs small" style="left:92px;top:561px;width:162px;text-align:center">Neque porro quisquam est qui dolorem ipsum quia dolor sit amet</p>
  <div class="abs btn green" style="left:142px;top:602px;width:61px">Learn More</div>

  <div class="abs card" style="left:278px;top:472px;width:184px;height:152px"></div>
  <h3 class="abs h3" style="left:278px;top:487px;width:184px">Events <em>&amp;</em> Happenings</h3>
  <div class="abs date" style="left:293px;top:522px">02</div>
  <p class="abs small" style="left:332px;top:522px;width:120px">Neque porro quisquam est qui dolor ipsum quia dolor.</p>
  <div class="abs date" style="left:293px;top:562px">05</div>
  <p class="abs small" style="left:332px;top:562px;width:120px">Neque porro quisquam est qui dolor ipsum quia dolor.</p>
  <div class="abs btn green" style="left:339px;top:602px;width:63px">Learn More</div>

  <div class="abs card" style="left:476px;top:472px;width:185px;height:152px"></div>
  <div class="abs" style="left:490px;top:490px;width:13px;height:13px;background:var(--green);border-radius:2px"></div>
  <h3 class="abs h3" style="left:510px;top:486px;text-align:left">Taproom feed</h3>
  <div class="abs avatar" style="left:488px;top:518px"></div>
  <div class="abs feed-name" style="left:526px;top:517px">Dana Kessler</div>
  <p class="abs small feed-text" style="left:526px;top:530px;width:128px">Neque porro quisquam est qu dolor ipsum quia dolor.</p>
  <div class="abs feed-link" style="left:526px;top:555px">Like &nbsp;::&nbsp; Comments</div>
  <div class="abs avatar" style="left:488px;top:578px"></div>
  <p class="abs small feed-text" style="left:526px;top:577px;width:128px">Neque porro quisquam est qu dolor ipsum quia dolor.</p>
  <div class="abs feed-link" style="left:526px;top:601px">Like &nbsp;::&nbsp; Comments</div>
</section>

<section>
  <h2 class="abs h3" style="left:0;top:659px;width:741px">Welcome to Craft Beer Company</h2>
  <p class="abs small" style="left:88px;top:693px;width:565px;text-align:center;font-size:8.3px;line-height:15px">Lorem ipsum dolor sit amet, consectetur adipiscing elit, sed do eiusmod tempor incididunt ut labore et dolore magna aliqua. Ut enim ad minim veniam, quis nostrud exercitation ullamco laboris nisi ut aliquip ex ea commodo consequat. Lorem ipsum dolor sit amet, consectetur adipiscing elit, sed do eiusmod tempor incididunt ut labore et dolore magna aliqua. Ut enim ad minim veniam, quis nostrud exercitation.</p>
  <div class="abs btn brown" style="left:335px;top:750px;width:71px">Learn More</div>
</section>

<section>
  <div class="abs" style="left:80px;top:802px;width:581px;height:326px;background:#f0f0f0"></div>
  <svg class="abs" style="left:98px;top:832px" width="10" height="12"><path d="M8 1L2 6l6 5" fill="none" stroke="#888" stroke-width="2"/></svg>
  <svg class="abs" style="left:633px;top:832px" width="10" height="12"><path d="M2 1l6 5-6 5" fill="none" stroke="#bbb" stroke-width="2"/></svg>
  <h2 class="abs h3" style="left:0;top:827px;width:741px">Featured <em>Products</em></h2>

  <article class="abs prod-card" style="left:100px;top:864px">
    <div class="abs prod-img" role="img" aria-label="Beer bottle with palm tree label" style="left:10px;top:10px;width:143px"></div>
    <div class="abs prod-name" style="left:0;top:150px;width:155px">Product Name</div>
    <p class="abs small" style="left:8px;top:170px;width:140px;text-align:center;font-size:7px;line-height:11px">Ut enim ad minim veniam, quis nos trud exercitation.</p>
    <div class="abs price" style="left:10px;top:198px">$220.00</div>
    <div class="abs btn brown" style="left:88px;top:199px;width:65px;line-height:18px">Add to Cart</div>
  </article>
  <article class="abs prod-card" style="left:288px;top:864px">
    <div class="abs prod-img" role="img" aria-label="Glass of amber ale beside a beer bottle" style="left:9px;top:10px;width:143px;background:linear-gradient(100deg,#e6e2da,#d4a04a 35%,#6a4a30 70%,#cfc9bf)"></div>
    <div class="abs prod-name" style="left:0;top:150px;width:155px">Product Name</div>
    <p class="abs small" style="left:8px;top:170px;width:140px;text-align:center;font-size:7px;line-height:11px">Ut enim ad minim veniam, quis nos trud exercitation.</p>
    <div class="abs price" style="left:9px;top:198px">$220.00</div>
    <div class="abs btn brown" style="left:87px;top:199px;width:65px;line-height:18px">Add to Cart</div>
  </article>
  <article class="abs prod-card" style="left:476px;top:864px">
    <div class="abs prod-img" role="img" aria-label="Beer bottle on a stone ledge" style="left:10px;top:10px;width:144px;background:linear-gradient(160deg,#8f8a84,#6a4a32 50%,#d9d6d0)"></div>
    <div class="abs prod-name" style="left:0;top:150px;width:155px">Product Name</div>
    <p class="abs small" style="left:8px;top:170px;width:140px;text-align:center;font-size:7px;line-height:11px">Ut enim ad minim veniam, quis nos trud exercitation.</p>
    <div class="abs price" style="left:10px;top:198px">$220.00</div>
    <div class="abs btn brown" style="left:89px;top:199px;width:65px;line-height:18px">Add to Cart</div>
  </article>
</section>

<footer>
  <div class="abs footer"></div>
  <div class="abs copy">Copyright © 2014 Yoursite. All rights reserved.</div>
  <div class="abs social" style="left:553px"></div>
  <div class="abs social" style="left:575px"></div>
  <div class="abs social" style="left:597px"></div>
  <div class="abs social" style="left:619px"></div>
  <div class="abs social" style="left:641px"></div>
</footer>

<div class="abs backdrop"></div>

<div class="abs modal" role="dialog" aria-label="Age verification">
  <div class="abs modal-bottle" role="img" aria-label="Beer bottle with sunset palm label"></div>
  <div class="abs modal-dot"></div>
  <div class="abs modal-brand">Harborline<br>Brewing</div>
  <p class="abs modal-q">Are you 21 years or older..</p>
  <label class="abs radio" style="left:88px"><i class="on"></i>Yes</label>
  <label class="abs radio" style="left:136px"><i></i>No</label>
  <div class="abs close">x</div>
</div>
</body>
</html>
```